Business Card Design

The new Company is called The Gilded Pecan - based in Miami Beach, Florida and Connecticut. We want a business card to be catchy and memorable ( like our Company name). Our business is marketing and retail sales of flavored cashew nuts in boutique /high end stores. The new business card must include a logo which must be a cashew nut with a king's crown or Roman wreath.
Yes- we are looking for a logo to be designed for the business and for the business card.

Industry/Entity Type

Marketing

Font styles to use
Script

```html
<!DOCTYPE html>
<html lang="en">
<head>
<meta charset="utf-8">
<title>The Gilded Pecan – Business Card</title>
<link href="https://fonts.googleapis.com/css2?family=Great+Vibes&family=Montserrat:wght@700&family=Questrial&display=swap" rel="stylesheet">
<style>
  :root {
    --page-bg: #ebe6de;
    --card-red-light: #d8264a;
    --card-red: #b3122c;
    --card-red-dark: #7e0714;
    --gold: #e2bf78;
    --gold-deep: #c99a4a;
    --ink-light: #ffffff;
    --ink-soft: #f6dede;
  }
  * { box-sizing: border-box; margin: 0; padding: 0; }
  html, body {
    width: 1200px;
    height: 1023px;
    overflow: hidden;
    background: var(--page-bg);
  }
  .business-card {
    position: absolute;
    left: 380px;
    top: 126px;
    width: 440px;
    height: 770px;
    border-radius: 6px;
    background: radial-gradient(ellipse at 50% 40%, var(--card-red-light) 0%, var(--card-red) 45%, var(--card-red-dark) 100%);
    box-shadow: 0 18px 40px rgba(60, 20, 20, 0.28);
    overflow: hidden;
    color: var(--ink-light);
  }
  .brand {
    position: absolute;
    top: 70px;
    left: 0;
    width: 100%;
    text-align: center;
  }
  .brand-dot {
    display: block;
    width: 96px;
    height: 96px;
    margin: 0 auto 26px;
    border-radius: 50%;
    background: var(--gold);
  }
  .brand-name {
    font-family: "Great Vibes", cursive;
    font-size: 56px;
    font-weight: 400;
    color: var(--ink-light);
    line-height: 1;
  }
  .gold-swoosh {
    position: absolute;
    left: 0;
    top: 330px;
    width: 440px;
    height: 200px;
  }
  .person {
    position: absolute;
    top: 400px;
    right: 44px;
    text-align: right;
  }
  .person-name {
    font-family: "Montserrat", sans-serif;
    font-weight: 700;
    font-size: 36px;
    line-height: 1.05;
  }
  .person-title {
    font-family: "Questrial", sans-serif;
    font-size: 22px;
    color: var(--ink-soft);
  }
  .contact-list {
    position: absolute;
    top: 510px;
    left: 44px;
    list-style: none;
    font-family: "Questrial", sans-serif;
    font-size: 17px;
    line-height: 1.35;
  }
  .contact-item {
    display: flex;
    align-items: flex-start;
    gap: 14px;
    margin-bottom: 16px;
  }
  .contact-icon {
    flex: none;
    width: 22px;
    height: 22px;
  }
</style>
</head>
<body>
  <article class="business-card">
    <header class="brand">
      <span class="brand-dot"></span>
      <h1 class="brand-name">The Gilded Pecan</h1>
    </header>

    <svg class="gold-swoosh" viewBox="0 0 440 200" aria-hidden="true">
      <path d="M10 190 C 40 90, 160 40, 440 55 C 190 55, 70 100, 10 190 Z" fill="var(--gold)"/>
    </svg>

    <div class="person">
      <p class="person-name">Mara Lowell</p>
      <p class="person-title">General Manager</p>
    </div>

    <ul class="contact-list">
      <li class="contact-item">
        <svg class="contact-icon" viewBox="0 0 24 24" aria-hidden="true">
          <path d="M6.6 3 L9.5 7.5 L7.6 9.6 C8.7 12 11 14.4 14.4 16.4 L16.5 14.5 L21 17.4 L19 21 C11 20.5 3.5 13 3 5 Z" fill="var(--ink-light)"/>
        </svg>
        <span>+1 305 555 0142</span>
      </li>
      <li class="contact-item">
        <svg class="contact-icon" viewBox="0 0 24 24" aria-hidden="true">
          <rect x="2" y="5" width="20" height="14" fill="var(--ink-light)"/>
          <path d="M2 5 L12 13 L22 5" fill="none" stroke="var(--card-red)" stroke-width="1.6"/>
        </svg>
        <span>mara@thegildedpecan.com</span>
      </li>
      <li class="contact-item">
        <svg class="contact-icon" viewBox="0 0 24 24" aria-hidden="true">
          <circle cx="12" cy="12" r="10" fill="none" stroke="var(--ink-light)" stroke-width="2"/>
          <ellipse cx="12" cy="12" rx="4.5" ry="10" fill="none" stroke="var(--ink-light)" stroke-width="1.5"/>
          <path d="M2 12 H22 M4 7 H20 M4 17 H20" stroke="var(--ink-light)" stroke-width="1.5"/>
        </svg>
        <span>www.thegildedpecan.com</span>
      </li>
      <li class="contact-item">
        <svg class="contact-icon" viewBox="0 0 24 24" aria-hidden="true">
          <path d="M12 2 C7.6 2 4.5 5.2 4.5 9.3 C4.5 14.5 12 22 12 22 C12 22 19.5 14.5 19.5 9.3 C19.5 5.2 16.4 2 12 2 Z" fill="var(--ink-light)"/>
          <circle cx="12" cy="9.3" r="2.8" fill="var(--card-red)"/>
        </svg>
        <span>48 Alder Crest lane<br>Coral Bay, FL 33139</span>
      </li>
    </ul>
  </article>
</body>
</html>
```